Web Design Project

Create a web design

Target Market(s)

Upper class people interested in health

Requirements
Must have
• Templates
Nice to have
• Use the logo provided

```html
<!DOCTYPE html>
<html lang="en">
<head>
<meta charset="utf-8">
<title>Verdant PT</title>
<link href="https://fonts.googleapis.com/css2?family=Raleway:wght@300&family=Noto+Sans:wght@400;700&family=Arimo:wght@400;700&display=swap" rel="stylesheet">
<style>
  :root {
    --green: #14a84a;
    --navy: #13295e;
    --nav-dark: #0a4a9c;
    --nav-light: #7ea8e4;
    --slide-dark: #2a4c9e;
    --slide-light: #5f86d6;
    --yellow: #ffd41c;
    --yellow-dark: #f3b600;
    --link-blue: #0a4a9c;
    --text: #6d6d6d;
    --heading: #2c2c2c;
    --rule: #d9d9d9;
    --footer: #333333;
    --white: #ffffff;
    --dot-teal: #2b8a9a;
  }
  * { box-sizing: border-box; margin: 0; padding: 0; }
  html, body { width: 834px; height: 1200px; overflow: hidden; background: var(--white); }
  body { position: relative; font-family: "Arimo", Arial, sans-serif; color: var(--text); }

  .top-rule { position: absolute; top: 0; left: 0; width: 834px; height: 3px; background: var(--green); }

  .brand { position: absolute; left: 88px; top: 14px; font-family: "Raleway", sans-serif; font-weight: 300; font-size: 46px; color: var(--navy); letter-spacing: -0.5px; }
  .call { position: absolute; right: 88px; top: 48px; color: var(--green); font-weight: 700; font-size: 12px; }
  .call strong { font-size: 17px; margin-left: 4px; }

  .main-nav { position: absolute; left: 33px; top: 94px; width: 768px; height: 41px; border-radius: 0 0 6px 6px;
    background: linear-gradient(90deg, var(--nav-dark) 0%, #2f6cc0 35%, var(--nav-light) 60%, #2f6cc0 78%, var(--nav-dark) 100%);
    display: flex; align-items: center; padding-left: 56px; gap: 23px; }
  .main-nav a { color: var(--white); text-decoration: none; font-weight: 700; font-size: 11px; text-shadow: 0 1px 1px rgba(0,0,0,.55); }

  .hero-figure { position: absolute; left: 100px; top: 150px; width: 200px; height: 362px;
    background: linear-gradient(180deg, #f1ece6 0%, #f5f1ec 50%, #ece6e0 100%); border-radius: 60px 60px 20px 20px; }

  .slide { position: absolute; left: 376px; top: 160px; width: 425px; height: 300px; border-radius: 5px;
    background: linear-gradient(135deg, var(--slide-light) 0%, #4a70c6 45%, var(--slide-dark) 100%);
    box-shadow: inset 0 0 0 6px rgba(255,255,255,.07); color: var(--white); }
  .slide h1 { position: absolute; left: 78px; top: 40px; font-size: 30px; font-weight: 700; letter-spacing: -0.5px; }
  .slide h1 span { color: var(--yellow); }
  .slide h2 { position: absolute; left: 111px; top: 72px; font-size: 13px; font-weight: 700; }
  .slide p { position: absolute; left: 111px; top: 125px; width: 212px; font-size: 11.5px; line-height: 21px; }
  .slide .btn { left: 234px; top: 229px; }

  .btn { position: absolute; display: inline-block; width: 88px; height: 26px; line-height: 26px; text-align: center; border-radius: 13px;
    background: linear-gradient(180deg, #ffe35a 0%, var(--yellow) 50%, var(--yellow-dark) 100%); color: var(--link-blue);
    font-weight: 700; font-size: 12.5px; text-decoration: none; border: 1px solid #f0c23a; }

  .dots { position: absolute; left: 538px; top: 478px; display: flex; gap: 6px; }
  .dots i { width: 15px; height: 15px; border-radius: 50%; background: radial-gradient(circle at 40% 35%, #4e6fc4, #1e3780); }
  .dots i.active { background: radial-gradient(circle at 40% 35%, #c6d9fb, #6f95dd); }

  .mid-rule { position: absolute; left: 33px; top: 512px; width: 768px; height: 3px; background: var(--green); }

  .col h3 { font-weight: 400; font-size: 16px; color: var(--heading); }
  .col p { font-size: 11px; line-height: 15.6px; }
  .col p.lead { color: var(--heading); font-weight: 700; font-size: 10.7px; line-height: 16px; }

  .col-left { position: absolute; left: 33px; top: 540px; width: 278px; }
  .col-left p { width: 272px; }
  .col-left h3 { margin-bottom: 17px; }
  .col-left .lead { margin-bottom: 14px; }
  .col-left hr { border: 0; border-top: 1px solid var(--rule); margin: 16px 0 18px; }

  .col-mid { position: absolute; left: 345px; top: 540px; width: 294px; }
  .col-mid p { width: 270px; }
  .video { width: 294px; height: 165px; border: 1px solid #ddd; border-radius: 3px; padding: 3px; background: var(--white); }
  .video-frame { position: relative; width: 100%; height: 100%; background: linear-gradient(120deg, #3a2f2a 0%, #8a6f55 40%, #c9a57d 60%, #2b3344 100%); }
  .video-bar { position: absolute; left: 3px; right: 3px; bottom: 3px; height: 18px; background: rgba(20,20,20,.85); display: flex; align-items: center; gap: 6px; padding: 0 6px; font-size: 7px; color: #ccc; }
  .video-bar .track { flex: 1; height: 3px; background: #666; border-radius: 2px; }
  .col-mid h3 { margin: 18px 0 10px; }

  .col-right { position: absolute; left: 670px; top: 540px; width: 130px; }
  .col-right h3 { margin-bottom: 6px; }
  .side-list { list-style: none; margin-left: 2px; width: 100px; }
  .side-list li { height: 27px; line-height: 27px; border-bottom: 1px solid #e4e4e4; font-size: 10.5px; color: #555; padding-left: 28px; position: relative; }
  .side-list li:last-child { border-bottom: 0; }
  .side-list li::before { content: ""; position: absolute; left: 18px; top: 10px; width: 7px; height: 7px; border-radius: 50%; background: var(--dot-teal); }

  .col-left .btn { left: 188px; top: 313px; }
  .col-mid .btn { left: 187px; top: 313px; }

  .site-footer { position: absolute; left: 33px; top: 905px; width: 768px; height: 279px; background: var(--footer); border-radius: 6px; color: var(--white); font-family: "Noto Sans", sans-serif; }
  .site-footer h4 { font-size: 14.5px; font-weight: 700; margin-bottom: 14px; }
  .site-footer address { font-style: normal; font-size: 11.5px; line-height: 18px; }
  .f-col { position: absolute; top: 32px; }
  .f-one { left: 49px; }
  .f-two { left: 295px; }
  .f-follow { position: absolute; left: 294px; top: 150px; }
  .social { display: flex; gap: 9px; }
  .social span { width: 30px; height: 30px; border-radius: 6px; background: #8b8b8b; }
  .f-three { left: 540px; }
  .contact-form input, .contact-form textarea { display: block; border: 0; background: var(--white); font-family: "Noto Sans", sans-serif; font-size: 9.5px; color: #aaa; padding: 0 4px; }
  .contact-form input { width: 130px; height: 18px; margin-bottom: 8px; }
  .contact-form textarea { width: 180px; height: 98px; margin-top: 1px; background: linear-gradient(180deg, #eee, #fff 40%); resize: none; }
  .contact-form button { margin-top: 9px; width: 59px; height: 23px; border: 0; border-radius: 2px; background: linear-gradient(180deg, #fff, #ddd); font-family: "Noto Sans", sans-serif; font-weight: 700; font-size: 11.5px; color: #333; }
</style>
</head>
<body>
  <div class="top-rule"></div>

  <header>
    <div class="brand">Verdant PT</div>
    <div class="call">Call <strong>(800) 555-0148</strong></div>
    <nav class="main-nav">
      <a href="#">HOME</a>
      <a href="#">FACILITIES</a>
      <a href="#">PROGAMRS &amp; FACILITIES</a>
      <a href="#">MEMBERSHIP</a>
      <a href="#">FREE TRIALS</a>
      <a href="#">NEWS EVENTS</a>
      <a href="#">RECRUITMENT</a>
    </nav>
  </header>

  <section class="hero">
    <div class="hero-figure" role="img" aria-label="Photo of a fit woman in white sportswear"></div>
    <div class="slide">
      <h1>VITA <span>PERFECTA</span></h1>
      <h2>An Nullam Alterum</h2>
      <p>In legere probatus ius, iuvaret contentiones ei sed. Qui in adhuc gubergren vituperatoribus, erat movet inimicus vis at. Ne affert postea eum, ex</p>
      <a class="btn" href="#">Read more</a>
    </div>
    <div class="dots"><i></i><i class="active"></i><i></i><i></i><i></i></div>
  </section>

  <div class="mid-rule"></div>

  <main>
    <article class="col col-left">
      <h3>Eu eam detracto repudiare</h3>
      <p class="lead">Cu ceteros dissentiunt vix, at eos assum melius volumus. Nec et erant clita consul, ius eu mazim</p>
      <p>Cu ceteros dissentiunt vix, at eos assum melius volumus. Nec et erant clita consul, ius eu mazim nullam euripidis, his velit percipit et. Eam mundi prompta ad, option apeirian vivendum ei ius, his option lobortis eu. In natum nullam volumus mel, vim ne albucius assueverit. Duo ea errem invidunt persequeris.</p>
      <hr>
      <p>Cu ceteros dissentiunt vix, at eos assum melius volumus. Nec et erant clita consul, ius eu mazim nullam euripidis, his velit percipit et. Eam mundi prompta ad, option apeirian vivendum ei ius, his option lobortis eu. In natum nullam volumus mel, vim ne albucius assueverit. Duo ea errem invidunt persequeris.</p>
      <a class="btn" href="#">Read more</a>
    </article>

    <article class="col col-mid">
      <div class="video">
        <div class="video-frame" role="img" aria-label="Video still of a woman exercising in a gym">
          <div class="video-bar">
            <svg width="9" height="9" viewBox="0 0 9 9"><path d="M1 0 L9 4.5 L1 9Z" fill="#ddd"/></svg>
            <span>00:00</span><span class="track"></span><span>01:00</span>
          </div>
        </div>
      </div>
      <h3>Eu eam detracto repudiare</h3>
      <p>Cu ceteros dissentiunt vix, at eos assum melius volumus. Nec et erant clita consul, ius eu mazim nullam euripidis, his velit percipit et. Eam mundi prompta ad, option apeirian vivendum ei ius, his option lobortis eu. In natum nullam volumus mel, vim ne albucius assueverit. Duo ea errem invidunt persequeris.</p>
      <a class="btn" href="#">Read more</a>
    </article>

    <aside class="col col-right">
      <h3>Eu eam detracto</h3>
      <ul class="side-list">
        <li>Reformidans</li><li>Iuvaret</li><li>Consequuntur</li><li>Ullamcorper</li><li>Essent</li><li>Gloriatur</li><li>Dicam</li><li>Primis</li><li>Scriptorem</li><li>Nulla</li><li>Dolore</li>
      </ul>
    </aside>
  </main>

  <footer class="site-footer">
    <div class="f-col f-one">
      <h4>Iriure Invidunt</h4>
      <address>418 Linden Row Suite #12<br>Maple Falls, ON 20480<br>Phone : +1 415.555.0193<br>Fax : +1 415.555.0194<br>hello@verdant.test</address>
    </div>
    <div class="f-col f-two">
      <h4>Iriure Invidunt</h4>
      <address>418 Linden Row Suite #12<br>Maple Falls, ON 20480<br>hello@verdant.test</address>
    </div>
    <div class="f-follow">
      <h4>Follow Us</h4>
      <div class="social"><span></span><span></span><span></span><span></span></div>
    </div>
    <div class="f-col f-three">
      <h4>Contact Us</h4>
      <form class="contact-form">
        <input type="text" placeholder="Name">
        <input type="text" placeholder="Email">
        <textarea></textarea>
        <button type="button">Send</button>
      </form>
    </div>
  </footer>
</body>
</html>
```